Two flyers with cover pages for business services company

We need to create two double sided A4 flyers for our company. We are a company that provides professional services for businesses in Dubai, UAE.
Please note that there are two different flyers. The design must be identical. Each has a cover page. The cover page will be duplicated for both flyers.
Please note that we have added images of the Dubai skyline, clip art as place-hold/temporary images. These can be changed to be more fitting to your design. We prefer to have free images where possible but are open to purchasing Pixelorra images if required.
We have recommended a colour palet below. You are welcome to change some colours to be more fitting to the design. However, we must have black, white and blue and per the logo.
Target Market(s)
Businesses, entrepreneurs, professionals
Industry/Entity Type
Business Service
Requirements
Must have
- The cover page should be less crowded and more visual. So mostly images with our logo and tagline.

```html
<!DOCTYPE html>
<html lang="en">
<head>
<meta charset="utf-8">
<title>Nexora Flyers</title>
<link href="https://fonts.googleapis.com/css2?family=Cabin:wght@400;500;600;700&family=Roboto+Condensed:wght@400;500&display=swap" rel="stylesheet">
<style>
:root{
  --bg:#e9ecf0;
  --white:#ffffff;
  --logo-blue:#1e8fe0;
  --logo-text:#3a3f4a;
  --blue-deep:#0c3f86;
  --blue-mid:#1a66b8;
  --blue-bright:#2a8be0;
  --cyan:#19b8ef;
  --navy:#0a2f6e;
  --yellow:#ffe21a;
  --ink:#2a2f38;
}
*{margin:0;padding:0;box-sizing:border-box}
html,body{width:1200px;height:785px;overflow:hidden;background:var(--bg)}
body{position:relative;font-family:"Cabin",Arial,sans-serif}
.flyer{position:absolute;top:59px;width:472px;height:666px;background:var(--blue-mid);overflow:hidden;box-shadow:0 4px 14px rgba(0,0,0,.25)}
.flyer--front{left:112px}
.flyer--back{left:616px}
.header{position:absolute;left:0;top:0;width:100%;height:87px;background:var(--white)}
.brand{position:absolute;left:40px;top:28px;display:flex;align-items:center;gap:8px}
.brand-dot{width:26px;height:26px;border-radius:50%;background:var(--logo-blue)}
.brand-name{font-size:31px;font-weight:500;color:var(--logo-text);letter-spacing:.5px;line-height:1}
.blue-field{position:absolute;left:0;width:100%;background:linear-gradient(180deg,var(--blue-bright),var(--blue-mid) 60%,var(--blue-deep))}
.block{position:absolute;background:rgba(255,255,255,.08)}
/* front */
.front-band{top:87px;height:136px}
.photo{position:absolute}
.photo-handshake{left:251px;top:87px;width:219px;height:126px;background:linear-gradient(135deg,#dfe6ee,#8a9bb0 55%,#3b4a63)}
.tagline-bar{position:absolute;left:0;top:223px;width:100%;height:41px;background:linear-gradient(90deg,#1d5aa8,#4d86c9 80%,#9cc0e8 88%,#c9dbef)}
.tagline{position:absolute;left:14px;top:7px;font-size:24px;font-weight:500;color:var(--white);letter-spacing:.3px}
.photo-skyline{left:0;top:268px;width:100%;height:262px;background:linear-gradient(180deg,#1a2f8a,#5a4f9e 40%,#c97aa6 62%,#2b2f55 78%,#141a2e)}
.front-foot{top:534px;height:132px}
/* back */
.back-field{top:87px;height:579px}
.headline{position:absolute;left:22px;top:94px;font-family:"Roboto Condensed",Arial,sans-serif;font-size:31px;line-height:34px;color:var(--yellow);font-weight:500}
.price-box{position:absolute;left:0;top:177px;width:100%;height:88px;background:var(--cyan);text-align:center;color:var(--white);font-size:28px;line-height:37px;padding-top:7px;font-weight:500}
.network{position:absolute;left:0;top:273px;width:100%;text-align:center;color:var(--white);font-size:14.5px;line-height:18px}
.network-lead{color:var(--yellow);font-weight:700;font-size:15px}
.offer-bar{position:absolute;left:0;top:347px;width:100%;height:47px;background:var(--navy);text-align:center;color:var(--white);font-size:25px;line-height:47px}
.photo-director{left:267px;top:421px;width:205px;height:220px;background:linear-gradient(180deg,rgba(63,120,196,.35),#2a4f86 55%,#1b2a44);z-index:1}
.perks{position:absolute;left:22px;top:410px;list-style:none;font-size:16px;line-height:21px;color:var(--white);z-index:2;white-space:nowrap}
.perk-title,.perk-note{color:var(--yellow);font-weight:400}
.perk{font-weight:700}
.contact{position:absolute;left:0;top:576px;width:267px;height:65px;background:var(--white);padding:7px 0 0 12px;font-size:8.6px;line-height:11.5px;color:var(--ink);font-style:normal;z-index:2}
.signature-strip{position:absolute;left:0;top:641px;width:100%;height:25px;background:linear-gradient(90deg,var(--blue-bright),var(--blue-mid))}
.director-label{position:absolute;right:8px;top:644px;width:197px;height:19px;background:var(--white);font-size:10px;line-height:19px;text-align:right;padding-right:4px;color:#111;font-weight:500;z-index:2}
</style>
</head>
<body>

<section class="flyer flyer--front">
  <header class="header">
    <div class="brand"><span class="brand-dot"></span><span class="brand-name">Nexora</span></div>
  </header>
  <div class="blue-field front-band">
    <span class="block" style="left:0;top:0;width:60px;height:60px"></span>
    <span class="block" style="left:120px;top:70px;width:110px;height:66px"></span>
    <span class="block" style="left:60px;top:60px;width:60px;height:76px"></span>
  </div>
  <div class="photo photo-handshake" role="img" aria-label="Photo of two business people shaking hands"></div>
  <div class="tagline-bar"><p class="tagline">Your Business Our Connections</p></div>
  <div class="photo photo-skyline" role="img" aria-label="Photo of the Dubai skyline at dusk"></div>
  <div class="blue-field front-foot">
    <span class="block" style="left:0;top:0;width:100%;height:40px;background:rgba(10,40,110,.35)"></span>
    <span class="block" style="left:300px;top:40px;width:172px;height:92px"></span>
    <span class="block" style="left:380px;top:0;width:92px;height:132px"></span>
  </div>
</section>

<section class="flyer flyer--back">
  <header class="header">
    <div class="brand"><span class="brand-dot"></span><span class="brand-name">Nexora</span></div>
  </header>
  <div class="blue-field back-field">
    <span class="block" style="left:300px;top:0;width:172px;height:90px"></span>
    <span class="block" style="left:0;top:310px;width:140px;height:180px"></span>
  </div>
  <h1 class="headline">Do you need help to<br>increase your sales?</h1>
  <div class="price-box">As Low as AED1,500<br>Easy Monthly Installments</div>
  <div class="network">
    <p class="network-lead">Grow Your Business Through Our Extensive Network</p>
    <p>3000+ Business Connections | 570+ Decision Makers, MDs,<br>CEO’s, Head of Purchasing</p>
  </div>
  <div class="offer-bar">The Best Offer in the Industry</div>
  <div class="photo photo-director" role="img" aria-label="Portrait photo of the managing director in a suit"></div>
  <ul class="perks">
    <li class="perk-title">Sponsorship</li>
    <li class="perk">50% off your current sponsorship fees</li>
    <li class="perk">Free sponsorship for 12 months</li>
    <li class="perk">Low monthly installments</li>
    <li class="perk">(starting at AED 1,500)</li>
    <li class="perk-note">We are your active sponsor or strategic</li>
    <li class="perk-note">partner if you are need us to be</li>
  </ul>
  <address class="contact">
    Call us NOW for a FREE consultancy on 04 555 0192<br>
    Located at the Harbourline Business Tower, 24th Floor Dubai, UAE<br>
    Sunday – Thursday: 9:00 am -18:00 pm<br>
    W: www.nexora.ae
  </address>
  <div class="signature-strip"></div>
  <p class="director-label">Daniel Marsh, Managing Director, Nexora</p>
</section>

</body>
</html>
```